Redesign Login page

I want to redesign my login page to bring my 2 products closer together. I am only looking to redesign one login page, not 2.

For the logo, please make it solid and it can be black or white if helpful. I can also fine tune the logo if you get it close.

Coding

Coded - Design and coding required

Number of Pages Required

1 page

```html
<!DOCTYPE html>
<html lang="en">
<head>
<meta charset="UTF-8">
<title>Sign in – Novaline</title>
<link rel="stylesheet" href="https://fonts.googleapis.com/css2?family=Poppins:wght@400;500;700&display=swap">
<style>
  :root {
    --page-bg: #ffffff;
    --card-bg: #ffffff;
    --card-glow: rgba(168, 150, 90, 0.75);
    --brand-red: #a3311f;
    --brand-olive: #7a6a14;
    --field-bg: #efefef;
    --text-dark: #1e1e1e;
    --text-muted: #6f6f6f;
    --checkbox-border: #c4c4c4;
  }
  * { box-sizing: border-box; margin: 0; padding: 0; }
  html, body {
    width: 1016px;
    height: 1200px;
    overflow: hidden;
    background: var(--page-bg);
    font-family: "Poppins", sans-serif;
    color: var(--text-dark);
  }
  .login-card {
    position: absolute;
    left: 137px;
    top: 132px;
    width: 751px;
    height: 945px;
    background: var(--card-bg);
    border-radius: 58px;
    box-shadow: 0 0 22px 4px var(--card-glow);
  }
  .welcome-heading {
    position: absolute;
    top: 66px;
    left: 0;
    width: 100%;
    text-align: center;
    font-size: 27px;
    font-weight: 400;
  }
  .brand-name {
    position: absolute;
    top: 132px;
    left: 0;
    width: 100%;
    text-align: center;
    font-size: 112px;
    font-weight: 700;
    letter-spacing: -2px;
    color: var(--brand-red);
    line-height: 1.2;
  }
  .field {
    position: absolute;
    left: 38px;
    width: 652px;
    height: 86px;
    border-radius: 43px;
    background: var(--field-bg);
  }
  .field-email { top: 395px; }
  .field-password { top: 508px; }
  .field-label {
    position: absolute;
    left: 44px;
    top: 16px;
    font-size: 19px;
    color: var(--text-muted);
  }
  .password-mask {
    position: absolute;
    left: 44px;
    top: 42px;
    font-size: 17px;
    letter-spacing: -1px;
    color: var(--text-muted);
  }
  .toggle-visibility {
    position: absolute;
    right: 34px;
    top: 28px;
    width: 34px;
    height: 30px;
  }
  .continue-button {
    position: absolute;
    left: 38px;
    top: 621px;
    width: 652px;
    height: 86px;
    border-radius: 43px;
    background: var(--brand-red);
    color: #ffffff;
    font-size: 27px;
    display: flex;
    align-items: center;
    justify-content: center;
  }
  .remember-me {
    position: absolute;
    left: 56px;
    top: 740px;
    display: flex;
    align-items: center;
    gap: 17px;
    font-size: 21px;
  }
  .checkbox {
    width: 29px;
    height: 29px;
    border: 2px solid var(--checkbox-border);
    border-radius: 4px;
  }
  .forgot-link {
    position: absolute;
    right: 80px;
    top: 740px;
    font-size: 21px;
    line-height: 29px;
    border-bottom: 1.5px solid var(--text-dark);
  }
  .signup-prompt {
    position: absolute;
    top: 825px;
    left: 0;
    width: 100%;
    text-align: center;
    font-size: 21px;
  }
  .signup-link {
    color: var(--brand-olive);
    border-bottom: 1.5px solid var(--brand-olive);
  }
</style>
</head>
<body>
  <main class="login-card">
    <h1 class="welcome-heading">Welcome To</h1>
    <div class="brand-name">Novaline</div>

    <div class="field field-email">
      <span class="field-label">Email</span>
    </div>

    <div class="field field-password">
      <span class="field-label">Password</span>
      <span class="password-mask">••••••••••</span>
      <svg class="toggle-visibility" viewBox="0 0 34 30" fill="none" stroke="#1e1e1e" stroke-width="2.2" stroke-linecap="round">
        <path d="M2 15 C8 6 26 6 32 15 C26 24 8 24 2 15 Z"/>
        <circle cx="17" cy="15" r="5"/>
        <line x1="5" y1="27" x2="29" y2="3"/>
      </svg>
    </div>

    <div class="continue-button">Continue</div>

    <label class="remember-me"><span class="checkbox"></span>Remember Me</label>
    <span class="forgot-link">Forgot Password?</span>

    <p class="signup-prompt">Don't have an account? <span class="signup-link">Sign up</span></p>
  </main>
</body>
</html>
```